Conflict prevention NGO needs business cards ASAP

We are a small NGO based in New Caledonia working on conflict prevention, and will be attending a OGA-sponsored conference on small arms next month. Our work involves campaigning against the proliferation of small arms in this post-conflict South Pacific island, and we need business cards to match that purpose.
Our three basic guidelines are the following:
1. We would like the logo of our organisation (see attached) included on this card. We are open to a redesign of this logo to something more stylised or abstract.
2. The card would need to be double-sided: one side in French, the other in English. The text should ideally be minimalist, uncluttered, clear and concise. We prefer the card to visually communicate our mission. As such, we would like the card to present a central image or logo, which would give us the option of printing a texture onto that image/logo later.
3. I have attached images which might inspire the designer (bullets and the famous knotted gun statue). However, these are NOT prescriptive; they are simply thematic ideas, and designers should use their own creative license. We only ask that the overall business card communicate professionalism and a seriousness of purpose, rather than sentimentalism or idealism.
Thanks to everyone who is willing to offer up a design idea! I am grateful for your time, and look forward to viewing your ideas. I apologise, but this has to be a rush job. Please get in touch if you need further guidance.
Please note that our new website will go live on Wednesday evening (Brisbane time), in case it can provide inspiration: http://www.portlumineux.org/
ENGLISH SIDE
[Name, Position] Kieran Vasko, Director
[Organisation] The Centre for a Bright Harbour
[Sub-Title] The first New Caledonian think tank
[Tel] +61407913222
[Email] centreportlumineux@postvale.net
[Website] http://www.portlumineux.org/
FRENCH SIDE
[Name, Position] Kieran Vasko, Directeur
[Organisation] Le Centre pour le Port Lumineux
[Sub-Title] Le premier pôle de réflexion calédonien
[Tel] +61407913222
*Note: We are flexible on the exact way you present the above information, and you may wish to use icons instead of "Tel." for example.

```html
<!DOCTYPE html>
<html lang="en">
<head>
<meta charset="utf-8">
<title>Business Cards – The Centre for a Bright Harbour</title>
<link rel="stylesheet" href="https://fonts.googleapis.com/css2?family=Arimo:wght@400;700&family=Open+Sans:wght@400&display=swap">
<style>
  :root {
    --backdrop: #ececec;
    --card: #ffffff;
    --card-edge: #6a6a6a;
    --navy: #1f4690;
    --brand-blue: #1c5fa8;
    --rule-green: #2fa84a;
    --ink: #ffffff;
    --muted: #555a60;
  }
  * { box-sizing: border-box; margin: 0; padding: 0; }
  html, body { width: 1084px; height: 1200px; overflow: hidden; }
  body {
    background: var(--backdrop);
    position: relative;
    font-family: "Arimo", Arial, sans-serif;
  }
  .card {
    position: absolute;
    left: 108px;
    width: 870px;
    height: 497px;
    background: var(--card);
    border: 1px solid var(--card-edge);
  }
  .card--french { top: 73px; }
  .card--english { top: 623px; }

  .brand {
    position: absolute;
    left: 0; right: 0; top: 34px;
    display: flex; flex-direction: column; align-items: center;
  }
  .brand__square {
    width: 150px; height: 150px;
    background: var(--brand-blue);
  }
  .brand__name {
    margin-top: 18px;
    font-weight: 700;
    font-size: 26px;
    color: var(--brand-blue);
    letter-spacing: 0.5px;
  }

  .rule {
    position: absolute; left: 0; right: 0;
    height: 2px; background: var(--rule-green);
  }
  .rule--top { top: 288px; }
  .rule--bottom { top: 375px; }

  .title-band {
    position: absolute; left: 0; right: 0; top: 298px; height: 70px;
    background: var(--navy);
    display: flex; align-items: center; justify-content: center;
    color: var(--ink);
    white-space: nowrap;
  }
  .title-band__name { font-weight: 700; font-size: 32px; margin-right: 8px; }
  .title-band__role { font-size: 23px; margin-right: 8px; }
  .title-band__org { font-size: 22px; }

  .contacts {
    position: absolute; left: 0; right: 0; top: 398px;
    font-family: "Open Sans", Arial, sans-serif;
    font-size: 21px; color: var(--muted);
    display: flex; flex-direction: column; align-items: center; gap: 12px;
  }
  .contacts__row { display: flex; align-items: center; gap: 24px; }
  .contact { display: flex; align-items: center; gap: 8px; }
  .contact__icon { width: 18px; height: 18px; fill: none; stroke: var(--navy); stroke-width: 2; }
</style>
</head>
<body>

  <section class="card card--french" lang="fr">
    <div class="brand">
      <div class="brand__square"></div>
      <div class="brand__name">Port Lumineux</div>
    </div>
    <div class="rule rule--top"></div>
    <div class="title-band">
      <span class="title-band__name">Kieran Vasko,</span>
      <span class="title-band__role">Directeur,</span>
      <span class="title-band__org">Le Centre pour le Port Lumineux</span>
    </div>
    <div class="rule rule--bottom"></div>
    <div class="contacts">
      <div class="contacts__row">
        <span class="contact">
          <svg class="contact__icon" viewBox="0 0 20 20"><path d="M5 2 L8 6 L6 8 Q8 12 12 14 L14 12 L18 15 L16 18 Q8 18 3 10 Q2 6 5 2 Z"/></svg>
          +61407913222
        </span>
        <span class="contact">
          <svg class="contact__icon" viewBox="0 0 20 20"><rect x="2" y="5" width="16" height="11"/><path d="M2 5 L10 11 L18 5"/></svg>
          centreportlumineux@postvale.net
        </span>
      </div>
      <span class="contact">
        <svg class="contact__icon" viewBox="0 0 20 20"><circle cx="10" cy="10" r="8"/><ellipse cx="10" cy="10" rx="3.5" ry="8"/><path d="M2 10 H18"/></svg>
        www.portlumineux.org
      </span>
    </div>
  </section>

  <section class="card card--english" lang="en">
    <div class="brand">
      <div class="brand__square"></div>
      <div class="brand__name">Bright Harbour</div>
    </div>
    <div class="rule rule--top"></div>
    <div class="title-band">
      <span class="title-band__name">Kieran Vasko,</span>
      <span class="title-band__role">Director,</span>
      <span class="title-band__org">The Centre for a Bright Harbour</span>
    </div>
    <div class="rule rule--bottom"></div>
    <div class="contacts">
      <div class="contacts__row">
        <span class="contact">
          <svg class="contact__icon" viewBox="0 0 20 20"><path d="M5 2 L8 6 L6 8 Q8 12 12 14 L14 12 L18 15 L16 18 Q8 18 3 10 Q2 6 5 2 Z"/></svg>
          +61407913222
        </span>
        <span class="contact">
          <svg class="contact__icon" viewBox="0 0 20 20"><rect x="2" y="5" width="16" height="11"/><path d="M2 5 L10 11 L18 5"/></svg>
          centreportlumineux@postvale.net
        </span>
      </div>
      <span class="contact">
        <svg class="contact__icon" viewBox="0 0 20 20"><circle cx="10" cy="10" r="8"/><ellipse cx="10" cy="10" rx="3.5" ry="8"/><path d="M2 10 H18"/></svg>
        www.portlumineux.org
      </span>
    </div>
  </section>

</body>
</html>
```